VFX Company Business Card Design Project

The Ember Vale is a decentralized Visual Effects Studio servicing the television and feature film industries.
Project Brief:
Take our logo that was previously designed on Pixel Harbor and make a double sided business card.
Requirements:
- Card MUST be double sided.
- Front of card MUST have the yellow part of our logo against the dark grey background.
- Back of card is completely up to the designer.
- Back of card must include the complete company logo.
Please follow these File Preparation guidelines:
http://printmoor.example/infopage?file=filetype_en&s=PrintMoor_new&lang=en
Industry/Entity Type
Business
Look and feel
Each slider illustrates characteristics of the customer's brand and the style your logo design should communicate.

```html
<!DOCTYPE html>
<html lang="en">
<head>
<meta charset="utf-8">
<title>The Ember Vale – Business Card</title>
<link rel="stylesheet" href="https://fonts.googleapis.com/css2?family=Mulish:wght@400;600&display=swap">
<style>
  :root {
    --backdrop: #3b3b3b;
    --card: #262626;
    --accent: #fdc82f;
    --rule: #b8943a;
    --text-light: #e6e6e6;
    --text-muted: #cfcfcf;
  }
  * { margin: 0; padding: 0; box-sizing: border-box; }
  html, body {
    width: 1200px; height: 900px; overflow: hidden;
    background: var(--backdrop);
    font-family: "Mulish", sans-serif;
  }
  .stage { position: relative; width: 1200px; height: 900px; }
  .card {
    position: absolute; top: 293px;
    width: 514px; height: 314px;
    background: var(--card);
    box-shadow: 0 4px 10px rgba(0,0,0,0.45);
    overflow: hidden;
  }
  .card--front { left: 72px; }
  .card--back { left: 614px; }

  .brand {
    color: var(--accent);
    font-weight: 600;
    white-space: nowrap;
    display: flex; align-items: center;
  }
  .brand__dot {
    display: inline-block; border-radius: 50%;
    background: var(--accent);
  }

  .card--front .brand {
    position: absolute; left: 0; right: 0; top: 132px;
    justify-content: center; gap: 16px;
    font-size: 40px; letter-spacing: 1px;
  }
  .card--front .brand__dot { width: 30px; height: 30px; }

  .card--back .brand {
    position: absolute; left: 36px; top: 42px;
    gap: 14px; font-size: 36px; letter-spacing: 1px;
  }
  .card--back .brand__dot { width: 30px; height: 30px; }

  .divider {
    position: absolute; left: 0; right: 0; top: 131px;
    height: 2px; background: var(--rule);
  }

  .person { position: absolute; left: 46px; top: 196px; }
  .person__name { color: var(--accent); font-size: 21px; font-weight: 400; line-height: 1.2; }
  .person__role { color: var(--text-light); font-size: 14px; line-height: 1.3; }

  .contacts {
    position: absolute; left: 284px; top: 160px;
    list-style: none; color: var(--text-muted);
    font-size: 13px; line-height: 16px;
  }
  .contacts__group { display: flex; flex-direction: column; margin-bottom: 16px; }
  .contacts__item { display: flex; align-items: flex-start; gap: 6px; }
  .contacts__icon { width: 11px; height: 11px; margin-top: 3px; flex: none; fill: var(--accent); }
  .contacts__spacer { width: 11px; flex: none; }
</style>
</head>
<body>
<main class="stage">
  <section class="card card--front" aria-label="Card front">
    <div class="brand"><span class="brand__dot"></span>The Ember Vale</div>
  </section>

  <section class="card card--back" aria-label="Card back">
    <div class="brand"><span class="brand__dot"></span>The Ember Vale</div>
    <div class="divider"></div>

    <div class="person">
      <p class="person__name">Marcus Hollander</p>
      <p class="person__role">managing director</p>
    </div>

    <ul class="contacts">
      <li class="contacts__group">
        <span class="contacts__item">
          <svg class="contacts__icon" viewBox="0 0 12 12"><path d="M6 0a4 4 0 0 0-4 4c0 3 4 8 4 8s4-5 4-8a4 4 0 0 0-4-4zm0 5.5A1.5 1.5 0 1 1 6 2.5a1.5 1.5 0 0 1 0 3z"/></svg>
          48 Larkfield Road
        </span>
        <span class="contacts__item"><span class="contacts__spacer"></span>Brookhaven, New York 10231</span>
      </li>
      <li class="contacts__group">
        <span class="contacts__item">
          <svg class="contacts__icon" viewBox="0 0 12 12"><path d="M3 0h6v12H3zM4 1.5v7.5h4V1.5z"/></svg>
          212 404 17 63
        </span>
        <span class="contacts__item">
          <svg class="contacts__icon" viewBox="0 0 12 12"><path d="M3 1h6v3H3zM1 5h10v5H9V8H3v2H1zM3 9h6v3H3z"/></svg>
          212 404 17 64
        </span>
      </li>
      <li class="contacts__group">
        <span class="contacts__item">
          <svg class="contacts__icon" viewBox="0 0 12 12"><path d="M0 2h12v8H0zM1 3l5 4 5-4z"/></svg>
          info@embervale.example
        </span>
        <span class="contacts__item">
          <svg class="contacts__icon" viewBox="0 0 12 12"><circle cx="6" cy="6" r="5.5"/><path d="M0.5 6h11M6 0.5v11" stroke="#262626" stroke-width="1"/></svg>
          www.embervale.example
        </span>
      </li>
    </ul>
  </section>
</main>
</body>
</html>
```